Medical practice in the United States needs a landing page

Our medical practice, based in Dallas, Texas, is called 'Talwick Headache Clinics.' We perform the Talwick Method on patients to treat chronic, severe head pain.

We currently have a landing page for our Chatterly ads, but we'd like to improve the page's design to increase the lead conversion rate. The landing page contains a form that allows people to register for our free, on-demand informational webinar about the procedure. Either part of the registration form or all of the registration form must be above the fold.

Here is the link to the landing page that needs a more attractive design: https://talwickheadache.example/migraine-treatment-webinars/talwick-treatment-free-patient-webinar/

Once a lead submits the registration form on that page, they are redirected to a different page on the site that contains the webinar video.

Here is a direct link to the page that contains the actual video (note: this is NOT the page for which I am requesting an improved design for this project; I am only including this link so that you can watch the video if you think it will help you create a design for the other page):

https://talwickheadache.example/talwick-headache-clinics-patient-information-webinar/
Updates

Designs look the same

Hello all,

The designs so far have been very impressive! Thank you all for your hard work. Please don't feel compelled to use my exact wording, though, for the description of the webinar. The only requirement is that the form on the page be present and contain the same form fields.

Thanks again!

Target Market(s)

Patients with chronic, severe head pain

Industry/Entity Type

Healthcare

Requirements
Must have
• Either part of the registration form or all of the registration form must be above the fold.
Should not have
• The registration form located completely below the fold.

```html
<!DOCTYPE html>
<html lang="en">
<head>
<meta charset="utf-8">
<title>Talwick Headache Clinics – Free Patient Webinar</title>
<link href="https://fonts.googleapis.com/css2?family=Poppins:wght@400;500;600;700&display=swap" rel="stylesheet">
<style>
:root{
  --navy:#0d4a5e;
  --green:#8cc63f;
  --ink:#1d2327;
  --muted:#666d72;
  --field:#f4f4f4;
  --white:#fff;
}
*{box-sizing:border-box;margin:0;padding:0}
html,body{width:1200px;height:2224px;overflow:hidden}
body{font-family:'Poppins',sans-serif;color:var(--ink);background:var(--white);position:relative}
a{color:inherit;text-decoration:none}

.site-header{height:60px;display:flex;align-items:center;padding:0 112px}
.brand{font-size:21px;font-weight:400;color:var(--navy);letter-spacing:-.5px;width:268px;white-space:nowrap}
.header-info{display:flex;align-items:center;gap:8px;font-size:10px;line-height:15px;color:var(--ink)}
.header-info.address{width:343px}
.header-info.phones{width:211px}
.icon-dot{width:23px;height:23px;border-radius:50%;background:var(--navy);display:flex;align-items:center;justify-content:center;flex:none}
.btn{display:inline-flex;align-items:center;justify-content:center;background:var(--green);color:#fff;font-weight:700;font-size:12px;border-radius:4px;text-transform:uppercase}
.btn.header-cta{width:153px;height:42px}

.hero{position:relative;height:572px}
.hero-photo{position:absolute;inset:0;background:linear-gradient(90deg,#c9d4dc 0%,#e8ecef 25%,#f5f7f8 45%,#eef7fb 70%,#e6f4fa 100%)}
.form-card{position:absolute;left:532px;top:33px;width:555px;height:501px;background:#fff;border-radius:8px;padding:25px 25px}
.form-card h1{font-size:15px;font-weight:600;margin-bottom:7px}
.form-card .lead{font-size:10px;line-height:15.6px;color:var(--muted);margin-bottom:11px}
.field-grid{display:grid;grid-template-columns:246px 246px;column-gap:13px;row-gap:13px}
.field{height:37px;background:var(--field);border-radius:3px;font-size:10px;color:var(--muted);padding:0 11px;display:flex;align-items:center}
.hint{font-size:10px;line-height:12px;margin-top:-6px;color:var(--ink)}
.hint.note{font-size:9.5px;color:var(--muted)}
.hint b{font-weight:500;color:var(--ink)}
.field.message{height:84px;align-items:flex-start;padding-top:12px;margin-top:14px}
.agree{display:flex;align-items:center;gap:6px;font-size:10px;margin-top:8px}
.agree span.box{width:13px;height:13px;border:1px solid #777;border-radius:2px}
.btn.submit{width:159px;height:43px;margin-top:17px}

.section-title{text-align:center;font-size:18px;font-weight:600;text-transform:uppercase}
.why{height:412px;padding-top:46px}
.why-grid{display:flex;gap:26px;padding:0 112px;margin-top:20px}
.why-card{width:224px;height:267px;background:#fff;border-radius:8px;box-shadow:0 2px 14px rgba(0,0,0,.07);text-align:center;padding-top:31px}
.why-card .badge{width:73px;height:73px;border-radius:50%;background:var(--navy);margin:0 auto 22px;display:flex;align-items:center;justify-content:center}
.why-card h3{font-size:12.5px;font-weight:600;line-height:15px;height:37px;padding:0 52px}
.why-card p{font-size:11.5px;line-height:14.8px;color:var(--muted);padding:0 24px;margin-top:6px}

.restore{display:flex;height:374px}
.restore-photo{width:608px;background:linear-gradient(120deg,#d8dde2,#c9b9aa 50%,#e8e2dc)}
.restore-copy{flex:1;background:var(--green);color:#fff;padding:78px 62px}
.restore-copy h2{font-size:18px;font-weight:600;line-height:22px;text-transform:uppercase}
.restore-copy ul{list-style:none;margin-top:38px}
.restore-copy li{position:relative;padding-left:21px;font-size:12.5px;line-height:19px;margin-bottom:25px;width:385px}
.restore-copy li::before{content:"";position:absolute;left:0;top:5px;width:10px;height:10px;border-radius:50%;background:var(--navy)}

.stories{height:455px;padding-top:46px;background:linear-gradient(180deg,#fff 0%,#fff 45%,#e9e5e2 78%,#c9c3bf 100%)}
.story-grid{display:flex;gap:23px;padding:0 113px;margin-top:19px}
.story-card{width:309px;height:307px;background:#fff;border-radius:8px;text-align:center;padding-top:38px;box-shadow:0 2px 14px rgba(0,0,0,.06)}
.story-card .quote{font-size:110px;line-height:70px;height:64px;color:#ececec;font-weight:700;font-family:Georgia,serif}
.story-card h3{font-size:12.5px;font-weight:600;line-height:15px;padding:0 36px;margin-top:14px}
.story-card p{font-size:11.5px;line-height:15.5px;color:var(--muted);padding:0 30px;margin-top:20px;height:52px}
.link{font-size:12.5px;font-weight:600;color:var(--green);border-bottom:1.5px solid var(--green);display:inline-block;margin-top:8px}

.cta-band{height:171px;background:var(--green);display:flex;padding:36px 0 0 166px}
.cta-item{display:flex;gap:18px;width:463px}
.cta-item .badge{width:73px;height:73px;border-radius:50%;background:var(--navy);display:flex;align-items:center;justify-content:center;flex:none}
.cta-item h3{font-size:12.5px;font-weight:600;color:#fff;margin-top:6px}
.cta-item p{font-size:9.5px;line-height:15.6px;color:#fff;margin-top:6px;width:310px}
.cta-item a{display:inline-block;margin-top:10px;font-size:12.5px;font-weight:600;color:var(--navy);border-bottom:1.5px solid var(--navy)}

.site-footer{height:180px;background:var(--navy);color:#fff;display:flex;padding:30px 0 0 112px;font-size:11.3px;line-height:18.5px}
.footer-brand{width:309px}
.footer-brand .brand{color:#fff;display:block;padding-bottom:14px;border-bottom:1px solid rgba(255,255,255,.5);width:235px;font-size:20px}
.footer-brand small{display:block;font-size:11.3px;margin-top:25px}
.footer-col{width:193px}
.footer-col h4{font-size:11.5px;font-weight:600;margin-bottom:6px;text-transform:uppercase}
.footer-col.wide{width:147px}
.footer-col.addr{width:174px;padding-top:2px}
.footer-col.tel{padding-top:4px}
</style>
</head>
<body>

<header class="site-header">
  <div class="brand">talwick headache clinics</div>
  <div class="header-info address">
    <span class="icon-dot"><svg width="10" height="13" viewBox="0 0 10 13"><path d="M5 0C2.2 0 0 2.2 0 5c0 3.6 5 8 5 8s5-4.4 5-8c0-2.8-2.2-5-5-5z" fill="#8cc63f"/><circle cx="5" cy="5" r="1.8" fill="#0d4a5e"/></svg></span>
    <span>Talwick Headache Clinics Corporate Headquarters<br>2400 Harwell Parkway Suite 310 Dallas, Texas 75219</span>
  </div>
  <div class="header-info phones">
    <span class="icon-dot"><svg width="11" height="11" viewBox="0 0 24 24"><path d="M6.6 10.8a15 15 0 006.6 6.6l2.2-2.2c.3-.3.7-.4 1-.2 1.1.4 2.3.6 3.6.6.6 0 1 .4 1 1V20c0 .6-.4 1-1 1C10.6 21 3 13.4 3 4c0-.6.4-1 1-1h3.5c.6 0 1 .4 1 1 0 1.3.2 2.5.6 3.6.1.3 0 .7-.2 1z" fill="#8cc63f"/></svg></span>
    <span>Main: (844) 555-0147<br>After Hours: (972) 555-0183</span>
  </div>
  <a class="btn header-cta" href="#">Free Consult</a>
</header>

<section class="hero">
  <div class="hero-photo" role="img" aria-label="Smiling physician in a white coat holding the hands of an older patient in a bright clinic"></div>
  <form class="form-card">
    <h1>WEBINAR REGISTRATION FORM</h1>
    <p class="lead">Please fill out the form below to request a complimentary, obligation-free consultation with Dr. Talwick, the inventor of the Talwick Method®. Dr. Talwick will review your medical history and the Talwick Method® in detail and then spend all of the time necessary to answer all of your questions.</p>
    <div class="field-grid">
      <div class="field">First Name</div>
      <div class="field">Last Name</div>
      <div class="field">Email</div>
      <div class="field">Phone</div>
      <div class="field">Diagnosis</div>
      <div class="field">Insurance Carrier</div>
      <p class="hint">Please select the one that best applies to you.</p>
      <p class="hint note"><b>Note:</b> We do not accept Brightmere Health, Statecare Assist, or Workers' Compensation.</p>
    </div>
    <div class="field message">Message</div>
    <label class="agree"><span class="box"></span>I agree with the site's User Agreement and Privacy Policy.</label>
    <a class="btn submit" href="#">Request Consult</a>
  </form>
</section>

<section class="why">
  <h2 class="section-title">Why Talwick Headache Clinics?</h2>
  <div class="why-grid">
    <div class="why-card">
      <div class="badge"><svg width="34" height="34" viewBox="0 0 34 34"><circle cx="17" cy="17" r="16" fill="#8cc63f"/><path d="M10 17.5l5 5 9-10" stroke="#0d4a5e" stroke-width="3.5" fill="none" stroke-linecap="round" stroke-linejoin="round"/></svg></div>
      <h3>Documented Proven Success</h3>
      <p>Documented success rate of over 80% with over 100 peer-reviewed medical papers confirming success</p>
    </div>
    <div class="why-card">
      <div class="badge"><svg width="30" height="34" viewBox="0 0 30 34"><path d="M15 2C8 2 3 7 3 13c0 4 2 6 3 8v11h13v-5h5c1 0 2-1 2-2v-5l3-1-3-6C25 6 21 2 15 2z" fill="#8cc63f"/><circle cx="14" cy="12" r="4" fill="#0d4a5e"/></svg></div>
      <h3>World's Most Experienced</h3>
      <p>Talwick Headache specialists have been performing the Talwick Method since they invented it in 1992.</p>
    </div>
    <div class="why-card">
      <div class="badge"><svg width="44" height="26" viewBox="0 0 44 26"><path d="M2 3l8 2 4 14-6 2zM42 3l-8 2-4 14 6 2z" fill="#8cc63f"/><path d="M12 7l8-3 6 3 6-1 2 12-10 6-10-6z" fill="#8cc63f"/><path d="M18 12l5 5M21 10l5 5" stroke="#0d4a5e" stroke-width="1.6"/></svg></div>
      <h3>Research Partnerships</h3>
      <p>Partnered with Northfield Clinic and other leading institutions to bring the latest technology and discoveries.</p>
    </div>
    <div class="why-card">
      <div class="badge"><svg width="36" height="36" viewBox="0 0 36 36"><circle cx="18" cy="18" r="17" fill="#8cc63f"/><g fill="#0d4a5e"><circle cx="18" cy="10" r="4"/><circle cx="18" cy="26" r="4"/><circle cx="10" cy="18" r="4"/><circle cx="26" cy="18" r="4"/><circle cx="18" cy="18" r="1.6"/></g></svg></div>
      <h3>In the Media</h3>
      <p>The Talwick Method has been documented in TV shows and on the news. As seen on Channel 8 News and Health Hour</p>
    </div>
  </div>
</section>

<section class="restore">
  <div class="restore-photo" role="img" aria-label="Doctor giving a high five to a smiling young girl seated on her mother's lap in an exam room"></div>
  <div class="restore-copy">
    <h2>Control your headaches.<br>Restore your life.</h2>
    <ul>
      <li>After struggling with hemiplegic migraines, Marla has an amazing response to the Talwick Method®.</li>
      <li>15-year-old Elise renews life after suffering 3 years of daily migraines.</li>
    </ul>
  </div>
</section>

<section class="stories">
  <h2 class="section-title">Patient Lives Restored – Migraine Free</h2>
  <div class="story-grid">
    <div class="story-card">
      <div class="quote">”</div>
      <h3>I returned to school and decided to switch to neuroscience.</h3>
      <p>“I was able to return to college and a fully active life. I am in control of my headaches now.”</p>
      <a class="link" href="#">Watch Video</a>
    </div>
    <div class="story-card">
      <div class="quote">”</div>
      <h3>A migraine for 27 months…the procedure changed my life completely.</h3>
      <p>“It's great. My headaches are gone. It's wonderful.”</p>
      <a class="link" href="#">Watch Video</a>
    </div>
    <div class="story-card">
      <div class="quote">”</div>
      <h3>I can go outside and take my girls to the park anytime.</h3>
      <p>“I got my life back. Migraine headaches had taken it away. I can play with my kids again.”</p>
      <a class="link" href="#">Watch Video</a>
    </div>
  </div>
</section>

<section class="cta-band">
  <div class="cta-item">
    <span class="badge"><svg width="34" height="34" viewBox="0 0 24 24"><path d="M6.6 10.8a15 15 0 006.6 6.6l2.2-2.2c.3-.3.7-.4 1-.2 1.1.4 2.3.6 3.6.6.6 0 1 .4 1 1V20c0 .6-.4 1-1 1C10.6 21 3 13.4 3 4c0-.6.4-1 1-1h3.5c.6 0 1 .4 1 1 0 1.3.2 2.5.6 3.6.1.3 0 .7-.2 1z" fill="#8cc63f"/></svg></span>
    <div>
      <h3>Call (844) 555-0147</h3>
      <p>Speak one-on-one with a Talwick Headache Clinics representative to see if you are a candidate and learn how the Talwick Method® may restore your life.</p>
      <a href="#">Call to Learn More</a>
    </div>
  </div>
  <div class="cta-item">
    <span class="badge"><svg width="38" height="34" viewBox="0 0 38 34"><rect x="1" y="1" width="36" height="24" rx="2" fill="#8cc63f"/><rect x="1" y="19" width="36" height="3" fill="#0d4a5e" opacity=".35"/><path d="M14 25h10l2 7H12z" fill="#8cc63f"/></svg></span>
    <div>
      <h3>Free On-Demand Webinar Available</h3>
      <p>Are you a good candidate for the Talwick Method®? Find the answer to this question and more by watching our free informational webinar!</p>
      <a href="#">View Webinar</a>
    </div>
  </div>
</section>

<footer class="site-footer">
  <div class="footer-brand">
    <span class="brand">talwick headache clinics</span>
    <small>Copyright © 2010-2023 All rights reserved.</small>
  </div>
  <div class="footer-col">
    <h4>We Offer</h4>
    FREE WEBINAR<br>Migraine Treatment<br>Talwick Method<br>Headache Help
  </div>
  <div class="footer-col wide">
    <h4>At a Glance</h4>
    Locations<br>Terms of Use<br>Privacy Policy<br>Sitemap<br>Contact
  </div>
  <div class="footer-col addr">Talwick Headache Clinics Corporate Headquarters<br>2400 Harwell Parkway<br>Suite 310<br>Dallas, Texas 75219</div>
  <div class="footer-col tel">Main: (844) 555-0147<br>or (214) 555-0126<br>After Hours: (972) 555-0183<br>Fax: (855) 555-0192</div>
</footer>

</body>
</html>
```